Fontenot Bayou Grillhouse (Owners Card)

Need a classy, but modern business card. I have included a promotional card for the steakhouse. I need one for myself (the owner) that is more professional.

Target Market(s)

General Public

Industry/Entity Type

Food service

Contact Information for Business Card

Name, business address, phone number, email, logo

Font styles to use
Serif
Sans Serif
Decorative
Script

Requirements
Must have
• My name (Darvel Pruitt), business address (327 Oakmere Street), phone number (510) 493-2615, email (Dpruittkr4@mailvane.example. On the back of the card: Psalms 27 1 The LORD is my light and my salvation— whom shall I fear? The LORD is the stronghold of my life— of whom shall I be afraid? 2 When the wicked advance against me to devour me, it is my enemies and my foes who will stumble and fall. 3 Though an army besiege me, my heart will not fear; though war break out against me, even then I will be confident.
Nice to have
• Something that’s bold, but modern and professional.

```html
<!DOCTYPE html>
<html lang="en">
<head>
<meta charset="utf-8">
<title>Fontenot Bayou Grillhouse – Owner Card</title>
<link rel="stylesheet" href="https://fonts.googleapis.com/css2?family=Cinzel:wght@700&family=Arimo:wght@400;700&display=swap">
<style>
  :root {
    --bg: #e4e4e4;
    --card: #f6f6f6;
    --ink: #222222;
    --red: #d40c12;
    --green: #12c400;
    --orange: #e88a00;
    --grad-green: #0bcf00;
    --grad-red: #e80400;
    --rule: #333333;
    --white: #ffffff;
  }
  * { box-sizing: border-box; margin: 0; padding: 0; }
  html, body { width: 1200px; height: 1040px; overflow: hidden; }
  body { background: var(--bg); font-family: "Arimo", Arial, sans-serif; color: var(--ink); position: relative; }

  .card { position: absolute; left: 284px; width: 644px; border-radius: 16px; overflow: hidden; }
  .card-front { top: 130px; height: 366px; background: var(--card); }
  .card-back { top: 567px; height: 369px; background: linear-gradient(90deg, var(--grad-green) 0%, var(--orange) 48%, var(--grad-red) 100%); color: var(--white); text-align: center; }

  .brand { position: absolute; left: 398px; top: 88px; width: 204px; display: flex; align-items: center; justify-content: center; gap: 8px; }
  .brand-dot { width: 14px; height: 14px; border-radius: 50%; background: var(--red); flex: none; }
  .brand-name { font-weight: 700; font-size: 17px; line-height: 1.2; color: var(--red); text-align: left; }

  .holder-name { position: absolute; left: 45px; top: 206px; font-family: "Cinzel", Georgia, serif; font-weight: 700; font-size: 25px; line-height: 1; color: var(--red); letter-spacing: 0.5px; }
  .holder-role { position: absolute; left: 46px; top: 236px; font-size: 16px; line-height: 18px; color: var(--green); }
  .divider { position: absolute; left: 45px; right: 44px; top: 259px; height: 1px; background: var(--rule); }

  .contact-list { position: absolute; left: 45px; top: 268px; list-style: none; font-size: 16px; line-height: 20px; }
  .contact-list li { display: flex; align-items: center; gap: 8px; }
  .contact-list svg { width: 13px; height: 13px; flex: none; }

  .address { position: absolute; right: 44px; top: 268px; text-align: right; font-size: 16px; line-height: 21px; font-style: normal; }

  .base-rule { position: absolute; left: 0; right: 0; bottom: 21px; height: 3px; background: #555555; }
  .base-band { position: absolute; left: 0; right: 0; bottom: 0; height: 18px; background: linear-gradient(90deg, var(--grad-green), var(--orange) 50%, var(--grad-red)); }

  .back-brand { position: absolute; left: 0; right: 0; top: 58px; display: flex; align-items: center; justify-content: center; gap: 12px; }
  .back-brand .brand-dot { width: 22px; height: 22px; background: var(--white); }
  .back-brand .brand-name { color: var(--white); font-size: 28px; }

  .verse-title { position: absolute; left: 0; right: 0; top: 157px; font-weight: 700; font-size: 20px; line-height: 22px; }
  .verse { position: absolute; left: 44px; right: 40px; font-size: 16px; line-height: 19px; }
  .verse-1 { top: 184px; line-height: 22px; }
  .verse-2 { top: 234px; }
  .verse-3 { top: 279px; }
  .back-web { position: absolute; left: 0; right: 0; top: 330px; font-weight: 700; font-size: 15px; letter-spacing: 3.5px; }
</style>
</head>
<body>

<section class="card card-front" aria-label="Business card front">
  <div class="brand">
    <span class="brand-dot"></span>
    <span class="brand-name">Fontenot Bayou<br>Grillhouse</span>
  </div>

  <h1 class="holder-name">Darvel Pruitt</h1>
  <p class="holder-role">Owner</p>
  <div class="divider"></div>

  <ul class="contact-list">
    <li>
      <svg viewBox="0 0 24 24" aria-hidden="true"><path fill="#d40c12" d="M6.6 10.8a15.1 15.1 0 0 0 6.6 6.6l2.2-2.2a1 1 0 0 1 1-.25 11.4 11.4 0 0 0 3.6.57 1 1 0 0 1 1 1V20a1 1 0 0 1-1 1A17 17 0 0 1 3 4a1 1 0 0 1 1-1h3.5a1 1 0 0 1 1 1c0 1.25.2 2.45.57 3.57a1 1 0 0 1-.25 1z"/></svg>
      (510) 493-2615
    </li>
    <li>
      <svg viewBox="0 0 24 24" aria-hidden="true"><rect x="2" y="5" width="20" height="14" fill="#d40c12"/><path d="M2 5l10 8 10-8" fill="none" stroke="#f6f6f6" stroke-width="2"/></svg>
      Dpruittkr4@mailvane.example
    </li>
    <li>
      <svg viewBox="0 0 24 24" aria-hidden="true"><circle cx="12" cy="12" r="10" fill="#d40c12"/><path d="M2 12h20M12 2c3 3 3 17 0 20M12 2c-3 3-3 17 0 20" fill="none" stroke="#f6f6f6" stroke-width="1.5"/></svg>
      www.Fontenotbayou.com
    </li>
  </ul>

  <address class="address">327 Oakmere Street<br>Larkdale, CA 94871</address>

  <div class="base-rule"></div>
  <div class="base-band"></div>
</section>

<section class="card card-back" aria-label="Business card back">
  <div class="back-brand">
    <span class="brand-dot"></span>
    <span class="brand-name">Fontenot Bayou Grillhouse</span>
  </div>
  <h2 class="verse-title">Psalms 27</h2>
  <p class="verse verse-1">The LORD is my light and my salvation— whom shall I fear?<br>The LORD is the stronghold of my life— of whom shall I be afraid?</p>
  <p class="verse verse-2">When the wicked advance against me to devour me, it is my enemies and<br>my foes who will stumble and fall.</p>
  <p class="verse verse-3">Though an army besiege me, my heart will not fear; though war break out<br>against me, even then I will be confident.</p>
  <p class="back-web">www.Fontenotbayou.com</p>
</section>

</body>
</html>
```